Flyer Design

We are a new service called quilvo.co.uk (see website) This is a premium rate £1:50 per sms text advice service. I am a qualified counsellor who already runs a practice see reslandcounselling.uk and have gotten per,it's ion from CALLMERIDIAN and are registered with them for this service. Quite simply they text Q7 followed by a brief description of their personal dilemma/life or relationship concern to 64391 this is received by me and then I text back with a brief piece of guidance and feedback on their issue. So it is a text based counselling/advice service for those who want a day to day life issue dealt with in confidence,quickly and discreetly. I want the flyers to be basic with a basic and easily transferable and identifiable image like the one on my website.

Industry/Entity Type

Counsellor

```html
<!DOCTYPE html>
<html lang="en">
<head>
<meta charset="utf-8">
<title>quilvo.co.uk flyer</title>
<link href="https://fonts.googleapis.com/css2?family=Londrina+Solid:wght@400;900&family=Open+Sans:wght@600&display=swap" rel="stylesheet">
<style>
:root{
  --backdrop:#d6d6d6;
  --sage:#93ada2;
  --bubble:#f8f8f5;
  --ink:#3a3d3d;
  --white:#ffffff;
  --skin:#f3e3c4;
  --suit:#4d535b;
}
*{margin:0;padding:0;box-sizing:border-box}
html,body{width:1200px;height:900px;overflow:hidden;background:var(--backdrop)}
body{position:relative;font-family:"Londrina Solid",sans-serif;color:var(--ink)}
.flyer{position:absolute;top:42px;width:566px;height:816px;background:var(--sage);overflow:hidden}
.flyer--front{left:30px}
.flyer--back{left:606px}
.site-title{position:absolute;top:14px;left:0;width:100%;text-align:center;font-weight:900;font-size:80px;letter-spacing:3px;line-height:1;color:var(--white);-webkit-text-stroke:2.5px var(--ink);paint-order:stroke fill}
.bubble-shape{position:absolute;left:0;top:0}
.figure{position:absolute}
.flyer--front .figure{left:292px;top:160px;width:274px;height:656px;background:linear-gradient(180deg,var(--skin) 0%,var(--skin) 55%,var(--suit) 70%,var(--suit) 100%);border-radius:120px 60px 0 0}
.flyer--back .figure{left:370px;top:470px;width:196px;height:346px;background:linear-gradient(180deg,var(--skin) 0%,var(--skin) 80%,var(--suit) 100%);border-radius:90px 40px 0 0}
.registered{position:absolute;right:22px;top:104px;text-align:left}
.registered__label{display:block;font-size:15px;letter-spacing:1px;color:var(--white);-webkit-text-stroke:1px var(--ink);paint-order:stroke fill}
.registered__name{display:block;font-family:"Open Sans",sans-serif;font-weight:600;font-size:20px;color:var(--white);letter-spacing:.5px}
.pitch{position:absolute;left:8px;top:130px;width:284px;text-align:center;text-transform:uppercase;color:var(--white);-webkit-text-stroke:1.6px var(--ink);paint-order:stroke fill}
.pitch__lead{font-size:31px;line-height:27px;letter-spacing:1px}
.pitch__lead+.pitch__lead{margin-top:25px}
.pitch__about{margin-top:30px;font-size:19px;line-height:17px;-webkit-text-stroke:1.2px var(--ink)}
.pitch__price{margin-top:16px;font-size:19px;line-height:17px;-webkit-text-stroke:1.2px var(--ink)}
.pitch__limit{margin-top:12px;font-size:12px;line-height:11px;-webkit-text-stroke:.8px var(--ink)}
.how{position:absolute;left:38px;top:130px;width:520px;text-transform:uppercase;font-size:13px;line-height:11px;letter-spacing:.4px}
.how h2{font-weight:400;font-size:17px;margin-bottom:20px}
.how p{margin-bottom:14px}
.small-print{position:absolute;left:24px;top:528px;width:330px;text-transform:uppercase;font-size:13px;line-height:11px;color:var(--white);-webkit-text-stroke:.8px var(--ink);paint-order:stroke fill}
.small-print p{margin-bottom:14px}
.social{position:absolute;left:96px;top:748px;display:flex;gap:10px}
.social__icon{width:50px;height:50px;border-radius:9px}
.social__icon--a{background:#2f5f9f}
.social__icon--b{background:#4fa8d8}
.social__icon--c{background:#e39430}
.social__icon--d{background:#e6e6e4}
</style>
</head>
<body>

<section class="flyer flyer--front">
  <h1 class="site-title">QUILVO.CO.UK</h1>
  <div class="registered">
    <span class="registered__label">REGISTERED WITH</span>
    <span class="registered__name">CALLMERIDIAN</span>
  </div>
  <div class="figure" role="img" aria-label="Illustration of a cartoon man in a grey suit and orange tie speaking"></div>
  <svg class="bubble-shape" width="566" height="816" aria-hidden="true">
    <path d="M30 106 Q8 106 8 130 L8 770 Q8 792 30 792 L268 792 Q292 792 292 770 L292 440 L316 425 L292 408 L292 130 Q292 106 268 106 Z" fill="var(--bubble)"/>
  </svg>
  <div class="pitch">
    <p class="pitch__lead">Need free,<br>confidential<br>advice?</p>
    <p class="pitch__lead">We help with:<br>work<br>health<br>relationships<br>family issues<br>&amp; much more!</p>
    <p class="pitch__lead">Just text Q7<br>followed by<br>your dilema<br>to<br>64391</p>
    <p class="pitch__about">We are qualified<br>counsellors with many<br>years experince of<br>dealing with a variety<br>of people from<br>adolescents to adults</p>
    <p class="pitch__price">Texts cost £1.50 + the<br>standard network fee</p>
    <p class="pitch__limit">Limited to 160<br>characters per text</p>
  </div>
</section>

<section class="flyer flyer--back">
  <h1 class="site-title">QUILVO.CO.UK</h1>
  <svg class="bubble-shape" width="566" height="816" aria-hidden="true">
    <path d="M40 106 Q20 106 20 126 L20 448 Q20 468 40 468 L230 468 L256 510 L262 468 L534 468 Q554 468 554 448 L554 126 Q554 106 534 106 Z" fill="var(--bubble)"/>
  </svg>
  <div class="how">
    <h2>How it works:</h2>
    <p>•You must get bill payers permission before using this service.</p>
    <p>We are a premium rate text support and guidance service operated by fully qualified practicing counsellors.</p>
    <p>It is simple &amp; straight forwrd. Simply start your message with either mate or Q7 followed by a brief description of your issue and send it to 64391.</p>
    <p>You will then receive a personalised response from a qualified and highly experience counsellor.</p>
    <p>You need not wrestle with life on your own nor do you need to rely on the biased advice of loved ones. There is no need to stay worried and anxious unclear and unsure. No more will you face the confusion of online search engine advice.</p>
    <p>Get support quickly and privately from the comfort and privacy of your own surroundings. From difficulties in work to problems in relationships or worries in yourself we are here to help.</p>
    <p>Counselling is a valuable and life changing experience but one that is not possible for everyone so we offer the same listening and non judgemental approach direct to your phone this of course can be read and kept or deleted if you need to.</p>
  </div>
  <div class="figure" role="img" aria-label="Illustration of the same cartoon man in a suit, shown from the shoulders up"></div>
  <div class="small-print">
    <p>We are a text based SMS support service run by trained, qualified and highly experienced counsellors</p>
    <p>Service operated by quilvo.co.uk</p>
    <p>Cust help tel: 07700 900214</p>
    <p>This is purely for customer technical issues and is not an extension of the quilvo.co.uk SMS service</p>
    <p>Must have bill payers permission. 16+ only.</p>
    <p>Full T's&amp;C's on our website, please read these before any contact</p>
    <p>To opt out of future marketing text stop to 64395</p>
  </div>
  <div class="social">
    <span class="social__icon social__icon--a"></span>
    <span class="social__icon social__icon--b"></span>
    <span class="social__icon social__icon--c"></span>
    <svg class="social__icon social__icon--d" viewBox="0 0 50 50" aria-label="Email">
      <rect x="11" y="15" width="28" height="20" rx="2" fill="none" stroke="#9a9a9a" stroke-width="2"/>
      <path d="M11 16 L25 27 L39 16" fill="none" stroke="#9a9a9a" stroke-width="2"/>
    </svg>
  </div>
</section>

</body>
</html>
```